dorwial business card design so that it looks better

need a new business card designed. use our website, dorwian.com for example. I attached an example of a previous card we had and liked. this is for law enforcement and we have attached a previous business card as an example. This site forces me to select color and font, ignore those as I picked stuff just to get this completed.

Target Market(s)

law enforcement, local government

Contact Information for Business Card

see the attached example and our website

Font styles to use
Serif

```html
<!DOCTYPE html>
<html lang="en">
<head>
<meta charset="utf-8">
<title>Dorwial Business Card</title>
<link href="https://fonts.googleapis.com/css2?family=Montserrat:wght@600&family=Arimo:wght@400;700&display=swap" rel="stylesheet">
<style>
  :root {
    --stage: #2b2b2f;
    --navy: #0b1a24;
    --ink: #0f1c26;
    --blue: #1f73c4;
    --white: #ffffff;
    --silver: #8d979e;
  }
  html, body {
    margin: 0;
    padding: 0;
    width: 1200px;
    height: 800px;
    overflow: hidden;
    background: var(--stage);
  }
  .sheet {
    position: relative;
    width: 1200px;
    height: 800px;
  }
  .card {
    position: absolute;
    top: 250px;
    width: 525px;
    height: 300px;
    overflow: hidden;
    box-shadow: 0 14px 30px rgba(0,0,0,0.45);
  }
  .card--back {
    left: 50px;
    background: var(--navy);
  }
  .card--front {
    left: 625px;
    background: var(--white);
  }
  .brand-name {
    position: absolute;
    font-family: "Montserrat", sans-serif;
    font-weight: 600;
    letter-spacing: 5px;
    margin: 0;
  }
  .card--back .brand-name {
    left: 0;
    right: 0;
    top: 118px;
    text-align: center;
    font-size: 50px;
    color: var(--silver);
  }
  .card--front .brand-name {
    left: 38px;
    top: 48px;
    font-size: 52px;
    color: var(--ink);
  }
  .person {
    position: absolute;
    left: 232px;
    top: 128px;
    font-family: "Arimo", sans-serif;
  }
  .person__name {
    margin: 0;
    font-weight: 700;
    font-size: 15px;
    color: var(--ink);
    letter-spacing: 0.3px;
  }
  .person__title {
    margin: 1px 0 0 18px;
    font-size: 14px;
    color: var(--blue);
  }
  .contact-rule {
    position: absolute;
    left: 0;
    right: 0;
    top: 206px;
    height: 2px;
    background: var(--blue);
  }
  .contact {
    position: absolute;
    top: 196px;
    width: 170px;
    margin-left: -85px;
    text-align: center;
    font-family: "Arimo", sans-serif;
    font-size: 13px;
    color: var(--ink);
  }
  .contact__icon {
    display: block;
    margin: 0 auto 8px;
    width: 22px;
    height: 22px;
  }
  .contact--phone { left: 100px; }
  .contact--mail { left: 268px; }
  .contact--web { left: 430px; }
  .address-band {
    position: absolute;
    left: 0;
    right: 0;
    bottom: 0;
    height: 42px;
    background: var(--navy);
    border-top: 2px solid var(--blue);
    color: var(--white);
    font-family: "Arimo", sans-serif;
    font-size: 13px;
    line-height: 42px;
    text-align: center;
    letter-spacing: 0.3px;
  }
</style>
</head>
<body>
<main class="sheet">
  <section class="card card--back" aria-label="Card back">
    <p class="brand-name">DORWIAL</p>
  </section>

  <section class="card card--front" aria-label="Card front">
    <p class="brand-name">DORWIAL</p>

    <div class="person">
      <p class="person__name">DANIEL REYES</p>
      <p class="person__title">Director</p>
    </div>

    <div class="contact-rule"></div>

    <div class="contact contact--phone">
      <svg class="contact__icon" viewBox="0 0 22 22" aria-hidden="true">
        <circle cx="11" cy="11" r="10" fill="#fff" stroke="#1f73c4" stroke-width="2"/>
        <path d="M8 6.5l1.6 2.2-1 1.2c.6 1.3 1.5 2.2 2.8 2.8l1.2-1 2.2 1.6-.9 1.6c-3.4-.3-6.2-3.1-6.5-6.5z" fill="#1f73c4"/>
      </svg>
      555.014.2290
    </div>

    <div class="contact contact--mail">
      <svg class="contact__icon" viewBox="0 0 22 22" aria-hidden="true">
        <circle cx="11" cy="11" r="10" fill="#fff" stroke="#1f73c4" stroke-width="2"/>
        <rect x="6" y="7.5" width="10" height="7" fill="#1f73c4"/>
        <path d="M6 7.5l5 4 5-4" fill="none" stroke="#fff" stroke-width="1"/>
      </svg>
      info@dorwian.com
    </div>

    <div class="contact contact--web">
      <svg class="contact__icon" viewBox="0 0 22 22" aria-hidden="true">
        <circle cx="11" cy="11" r="10" fill="#fff" stroke="#1f73c4" stroke-width="2"/>
        <circle cx="11" cy="11" r="5" fill="none" stroke="#1f73c4" stroke-width="1.2"/>
        <ellipse cx="11" cy="11" rx="2.2" ry="5" fill="none" stroke="#1f73c4" stroke-width="1"/>
        <path d="M6 11h10" stroke="#1f73c4" stroke-width="1"/>
      </svg>
      www.dorwian.com
    </div>

    <div class="address-band">4182 Marlow Avenue, Fairview, TX 75069</div>
  </section>
</main>
</body>
</html>
```